Im open to ideas.. I was thinking on my business cards aswell as my logo. a place for my name. email. phone number and abn..

ive attched a file with my business logo. which i dont love the colours.. i was think a dark background with charcoal letters so something along those colour schumes but im open to ideas..

Industry/Entity Type

Business

Logo Text

RLB Constructions

```html
<!DOCTYPE html>
<html lang="en">
<head>
<meta charset="utf-8">
<title>Vexmore Constructions – Business Card</title>
<link rel="stylesheet" href="https://fonts.googleapis.com/css2?family=Montserrat:wght@400;600;700&display=swap">
<style>
  :root {
    --page-bg: #e4e5e7;
    --card-bg: #000000;
    --brand-red: #ec1c24;
    --text-white: #ffffff;
    --rule-grey: #bdbdbd;
  }
  * { margin: 0; padding: 0; box-sizing: border-box; }
  html, body {
    width: 1200px;
    height: 924px;
    overflow: hidden;
    background: var(--page-bg);
    font-family: "Montserrat", sans-serif;
  }
  .canvas { position: relative; width: 1200px; height: 924px; }
  .business-card {
    position: absolute;
    left: 392px;
    top: 101px;
    width: 414px;
    height: 721px;
    background: var(--card-bg);
    color: var(--text-white);
    overflow: hidden;
    box-shadow: 6px 8px 14px rgba(0, 0, 0, 0.25);
  }
  .line {
    position: absolute;
    left: 0;
    width: 100%;
    text-align: center;
    white-space: nowrap;
  }
  .brand-name {
    top: 146px;
    font-weight: 700;
    font-size: 56px;
    line-height: 60px;
    letter-spacing: 4px;
    padding-left: 4px;
  }
  .brand-sub {
    top: 203px;
    font-weight: 700;
    font-size: 15px;
    line-height: 18px;
    letter-spacing: 12px;
    padding-left: 12px;
  }
  .divider {
    position: absolute;
    left: 90px;
    width: 229px;
    height: 3px;
    background: linear-gradient(90deg, transparent, var(--rule-grey) 15%, #ffffff 50%, var(--rule-grey) 85%, transparent);
  }
  .divider--top { top: 370px; }
  .divider--bottom { top: 591px; }
  .person-name {
    top: 385px;
    color: var(--brand-red);
    font-weight: 600;
    font-size: 29px;
    line-height: 34px;
    letter-spacing: 1px;
  }
  .person-role { top: 416px; font-size: 18.5px; line-height: 24px; }
  .abn { top: 443px; font-size: 19px; line-height: 24px; letter-spacing: 0.5px; }
  .abn-label { color: var(--brand-red); }
  .contact-icons {
    position: absolute;
    top: 482px;
    left: 0;
    width: 100%;
    display: flex;
    justify-content: center;
    gap: 6px;
    height: 14px;
  }
  .contact-icons svg { width: 14px; height: 14px; }
  .contact-line { font-size: 18px; line-height: 24px; letter-spacing: 0.3px; }
  .phone { top: 509px; }
  .email { top: 533px; }
  .website { top: 555px; }
  .bottom-band {
    position: absolute;
    left: 0;
    bottom: 0;
    width: 100%;
    height: 24px;
    background: var(--brand-red);
  }
</style>
</head>
<body>
<div class="canvas">
  <div class="business-card">
    <div class="line brand-name">VEXMORE</div>
    <div class="line brand-sub">CONSTRUCTIONS</div>

    <div class="divider divider--top"></div>

    <div class="line person-name">MARCUS REILLY</div>
    <div class="line person-role">Director</div>
    <div class="line abn"><span class="abn-label">ABN</span>: 61 482 305 719</div>

    <div class="contact-icons">
      <svg viewBox="0 0 14 14" aria-label="Phone">
        <path d="M3 1.5 L5 1.5 L5.8 4.3 L4.5 5.3 C5.2 7 6.8 8.6 8.6 9.4 L9.6 8.1 L12.4 8.9 L12.4 11 C12.4 11.8 11.7 12.5 10.9 12.4 C6 12 1.9 7.9 1.5 3 C1.4 2.2 2.1 1.5 3 1.5 Z" fill="none" stroke="#ec1c24" stroke-width="1.3"/>
      </svg>
      <svg viewBox="0 0 14 14" aria-label="Email">
        <rect x="1.5" y="3" width="11" height="8" fill="none" stroke="#ec1c24" stroke-width="1.3"/>
        <path d="M1.5 3 L7 7.5 L12.5 3" fill="none" stroke="#ec1c24" stroke-width="1.3"/>
      </svg>
      <svg viewBox="0 0 14 14" aria-label="Website">
        <circle cx="7" cy="7" r="5.6" fill="none" stroke="#ec1c24" stroke-width="1.2"/>
        <ellipse cx="7" cy="7" rx="2.4" ry="5.6" fill="none" stroke="#ec1c24" stroke-width="1"/>
        <path d="M1.4 7 H12.6 M2.2 4.2 H11.8 M2.2 9.8 H11.8" stroke="#ec1c24" stroke-width="1"/>
      </svg>
    </div>

    <div class="line contact-line phone">+330 2481-7320</div>
    <div class="line contact-line email">info@vexmoreconstructions.com</div>
    <div class="line contact-line website">www.vexmoreconstructions.com</div>

    <div class="divider divider--bottom"></div>

    <div class="bottom-band"></div>
  </div>
</div>
</body>
</html>
```